Personal Business Card Design Project

I am looking for a business card to be able to hand to both Chinese and Australian businessman.
I am a self employed consultant and just need my name, phone number and email address on the card. No Business Name and No Website.
I want it to look like an exclusive prestigious card.
I would like the background to be be a glossy red and the writing to be gold. (This applies to both sides of the card).
It must have English on one side and Chinese (Mandarin) on the reverse.
Details you will require
Name : Wade Emmerson
Phone : + 61 493 207 158
Email : wadeyemmerson@brightpost.example
Thank you everybody for your designs.
Industry/Entity Type
Business

```html
<!DOCTYPE html>
<html lang="en">
<head>
<meta charset="utf-8">
<title>Wade Emmerson – Business Card</title>
<link rel="stylesheet" href="https://fonts.googleapis.com/css2?family=Lato:wght@300;400&display=swap">
<style>
  :root {
    --page-bg: #ece8e2;
    --card-red: #d91f2a;
    --card-red-light: #ec3a44;
    --card-red-dark: #b5141e;
    --gold: #e8d29a;
    --gold-line: #dcc283;
  }
  html, body {
    margin: 0;
    width: 1200px;
    height: 1023px;
    overflow: hidden;
    background: var(--page-bg);
  }
  .business-card {
    position: absolute;
    left: 150px;
    top: 254px;
    width: 900px;
    height: 514px;
    background: linear-gradient(125deg, var(--card-red-light) 0%, var(--card-red) 45%, var(--card-red-dark) 100%);
    box-shadow: 0 18px 40px rgba(0,0,0,0.25);
    font-family: "Lato", sans-serif;
    color: var(--gold);
  }
  .card-name {
    position: absolute;
    left: 96px;
    bottom: 264px;
    margin: 0;
    font-weight: 300;
    font-size: 72px;
    letter-spacing: 1px;
    line-height: 1;
  }
  .card-divider {
    position: absolute;
    left: 96px;
    right: 0;
    top: 272px;
    height: 2px;
    background: var(--gold-line);
  }
  .card-contacts {
    position: absolute;
    left: 150px;
    top: 300px;
    margin: 0;
    padding: 0;
    list-style: none;
    font-weight: 400;
    font-size: 26px;
    line-height: 40px;
  }
  .contact-item {
    display: flex;
    align-items: center;
    gap: 14px;
  }
  .contact-icon {
    width: 22px;
    height: 22px;
    flex: none;
  }
</style>
</head>
<body>
  <div class="business-card">
    <h1 class="card-name">Wade Emmerson</h1>
    <div class="card-divider"></div>
    <ul class="card-contacts">
      <li class="contact-item">
        <svg class="contact-icon" viewBox="0 0 22 22" aria-hidden="true">
          <rect x="3" y="2" width="16" height="18" rx="1.5" fill="none" stroke="#e8d29a" stroke-width="1.8"/>
          <rect x="6" y="5" width="10" height="4" fill="#e8d29a"/>
          <g fill="#e8d29a">
            <rect x="6" y="11" width="2.4" height="2"/><rect x="9.8" y="11" width="2.4" height="2"/><rect x="13.6" y="11" width="2.4" height="2"/>
            <rect x="6" y="15" width="2.4" height="2"/><rect x="9.8" y="15" width="2.4" height="2"/><rect x="13.6" y="15" width="2.4" height="2"/>
          </g>
        </svg>
        <span>+ 61 493 207 158</span>
      </li>
      <li class="contact-item">
        <svg class="contact-icon" viewBox="0 0 22 22" aria-hidden="true">
          <rect x="2" y="4" width="18" height="14" fill="none" stroke="#e8d29a" stroke-width="1.8"/>
          <path d="M2 4 L20 18 M20 4 L2 18" stroke="#e8d29a" stroke-width="1.6"/>
        </svg>
        <span>wadeyemmerson@brightpost.example</span>
      </li>
    </ul>
  </div>
</body>
</html>
```